need a graphic redesign of kestrowcare.com

Need a graphic redesign of kestrowcare.com. We need to make it more user friendly as well as SEO friendly. All information is there. We have lot of stock photos (done our own photoshoot).

We want this website to be redesigned from scratch. Please avoid using pre made templates. Recommend people who really understand design to approach this project.

Target population is Non resident Indians who live outside India but their families are still in India and need for health care.

Logos and pictures are on the website but we can provide raw images.

Target Market(s)

Industry/Entity Type

Healthcare

Number of Pages Required

5+ page

Font styles to use
Serif
Sans Serif

Requirements
Must have
• Good design, and use of minimal text. Design need to be responsive (we know it is a later process in coding- but mobile devices need to be kept in mind)
Nice to have
• We need a original design.
Should not have
• prebuilt or copied templates

```html
<!DOCTYPE html>
<html lang="en">
<head>
<meta charset="utf-8">
<title>Kestrow Care</title>
<link href="https://fonts.googleapis.com/css2?family=Open+Sans:wght@300;400;600;700&display=swap" rel="stylesheet">
<style>
:root{
  --orange:#f39a1e;
  --green:#3a9e46;
  --dark:#262626;
  --nav:#333;
  --text:#555;
  --light:#f2f2f2;
  --line:#ddd;
  --white:#fff;
}
*{box-sizing:border-box;margin:0;padding:0}
html,body{width:1200px;height:2680px;overflow:hidden}
body{font-family:"Open Sans",sans-serif;color:var(--text);background:var(--white);position:relative}
.topbar{height:96px;display:flex;align-items:center;justify-content:space-between;padding:0 40px 0 60px}
.brand{display:flex;align-items:center;gap:12px;color:var(--green);font-weight:700;font-size:22px}
.brand .dot{width:26px;height:26px;border-radius:50%;background:var(--orange)}
.top-actions{display:flex;gap:12px}
.btn{display:inline-block;color:var(--white);font-size:13px;font-weight:600;padding:9px 22px;text-transform:uppercase;letter-spacing:.5px}
.btn-orange{background:var(--orange)}
.btn-green{background:var(--green)}
.mainnav{height:52px;background:var(--nav);display:flex;padding-left:60px}
.mainnav a{color:#ddd;font-size:13px;font-weight:600;padding:0 36px;line-height:52px;text-transform:uppercase}
.mainnav a.active{background:var(--orange);color:var(--white)}
.hero{position:relative;height:572px;background:linear-gradient(100deg,#e9e4df 0%,#cfd6dc 55%,#aeb7bf 100%)}
.hero-copy{position:absolute;right:40px;top:160px;width:520px}
.hero-copy h1{font-size:40px;font-weight:700;color:var(--dark);letter-spacing:2px;margin-bottom:16px}
.hero-copy p{background:rgba(255,255,255,.9);padding:18px 22px;font-size:15px;line-height:1.6;color:#444}
.hero-ctrl{position:absolute;top:260px;width:34px;height:34px;border-radius:50%;background:rgba(0,0,0,.35)}
.hero-ctrl.prev{left:20px}.hero-ctrl.next{right:20px}
.about{display:flex;gap:50px;padding:60px 60px 0;height:1180px - 720px}
.sec-title{font-size:28px;font-weight:300;color:var(--dark);text-transform:uppercase;letter-spacing:1px}
.sec-title b{color:var(--orange);font-weight:600}
.about-left{width:620px}
.tabs{display:flex;gap:6px;margin:22px 0}
.tabs span{font-size:12px;padding:8px 26px;background:var(--light);color:#666;text-transform:uppercase}
.tabs span.on{background:var(--orange);color:var(--white)}
.about-body{display:flex;gap:28px}
.ph{background:linear-gradient(160deg,#dfe3e6,#b9c2c9)}
.about-img{width:210px;height:200px;flex:none}
.about-body p{font-size:14px;line-height:1.6}
.about-body .btn{margin-top:16px;font-size:12px}
.about-right{flex:1}
.video{margin-top:22px;height:280px;position:relative;background:linear-gradient(180deg,#bfe3ef,#e7f2f4 60%,#c8ccd0)}
.video svg{position:absolute;left:50%;top:50%;transform:translate(-50%,-50%)}
.request{position:absolute;top:1180px;left:0;width:1200px;height:260px;background:linear-gradient(90deg,#3d3d3d,#555 50%,#3a3a3a);text-align:center;padding-top:40px}
.request .sec-title{color:#eee}
.form{width:760px;margin:28px auto 0;display:grid;grid-template-columns:1fr 1fr 1fr;gap:14px}
.field{background:var(--white);height:42px;font-size:13px;color:#999;text-align:left;padding:12px 14px}
.field.msg{grid-column:1/3;height:60px}
.submit{background:var(--orange);color:var(--white);font-weight:600;font-size:13px;height:42px;line-height:42px;align-self:end;letter-spacing:1px}
.team{position:absolute;top:1480px;left:0;width:1200px;text-align:center}
.team-grid{display:flex;justify-content:center;gap:26px;margin-top:40px}
.card{width:230px;border:1px solid var(--line);text-align:center;padding-bottom:20px}
.card .photo{height:190px;margin:12px}
.card h3{color:var(--orange);font-size:15px;font-weight:700;margin-top:6px}
.card .role{font-size:12px;color:#888;margin:2px 0 10px}
.card p{font-size:13px;line-height:1.5;padding:0 18px}
.pager{margin-top:22px;display:flex;justify-content:center;gap:8px}
.pager span{width:22px;height:22px;border-radius:50%;background:#999}
.partners{position:absolute;top:2020px;left:0;width:1200px;height:220px;background:var(--light);text-align:center;padding-top:44px}
.logos{display:flex;justify-content:center;gap:20px;margin-top:34px}
.logos span{width:150px;height:72px;background:var(--white);border:1px solid var(--line)}
.quote{position:absolute;top:2280px;left:0;width:1200px;text-align:center}
.quote .mark{font-size:64px;color:var(--green);font-weight:700;line-height:1}
.quote p{width:900px;margin:10px auto 22px;font-size:16px;line-height:1.6;color:#444}
.who{display:flex;justify-content:center;align-items:center;gap:14px;font-size:16px;color:var(--green);font-weight:600}
.who .avatar{width:60px;height:60px;border-radius:50%}
.footer{position:absolute;top:2520px;left:0;width:1200px;height:160px;background:var(--dark);color:#bbb;display:flex;justify-content:space-between;padding:40px 40px 0}
.footer h4{color:var(--white);font-weight:400;font-size:18px;letter-spacing:1px}
.contact{font-size:14px;line-height:1.7;text-align:center}
.contact .name{color:var(--white);font-weight:600}
.contact .name::before{content:"";display:inline-block;width:10px;height:10px;border-radius:50%;background:var(--orange);margin-right:8px}
.social{display:flex;gap:8px;justify-content:flex-end}
.social span{width:28px;height:28px;border-radius:50%;background:var(--white)}
.copy{font-size:13px;margin-top:14px;text-align:right}
</style>
</head>
<body>
<header class="topbar">
  <div class="brand"><span class="dot"></span>Kestrow Care</div>
  <div class="top-actions"><span class="btn btn-orange">Become Member</span><span class="btn btn-green">Login</span></div>
</header>
<nav class="mainnav">
  <a class="active">Home</a><a>About Us</a><a>Services</a><a>Our Network</a><a>Partner With Us</a><a>Contact Us</a>
</nav>
<section class="hero" role="img" aria-label="Doctor in white coat with stethoscope, medical staff in background">
  <span class="hero-ctrl prev"></span><span class="hero-ctrl next"></span>
  <div class="hero-copy">
    <h1>NEQUE PORRO QUISQUA</h1>
    <p>Kestrow Care is a company providing healthcare services to not only the elderly living in India, but their entire family. We focus on addressing the healthcare concerns of those who live abroad.</p>
  </div>
</section>
<section class="about" style="height:460px">
  <div class="about-left">
    <h2 class="sec-title">Get to know more <b>about us</b></h2>
    <div class="tabs"><span class="on">Who we are</span><span>What we do</span><span>Why us</span></div>
    <div class="about-body">
      <div class="about-img ph" role="img" aria-label="Smiling woman doctor"></div>
      <div>
        <p>Kestrow Care is a company providing healthcare services to not only the elderly living in India, but their entire family. We focus on addressing the healthcare concerns of those who have their children living abroad and assist them with the appropriate monitoring and maintenance of general health.</p>
        <span class="btn btn-orange">Read more</span>
      </div>
    </div>
  </div>
  <div class="about-right">
    <h2 class="sec-title">Featured <b>Video's</b></h2>
    <div class="video" role="img" aria-label="Video still of an ambulance in front of a hospital">
      <svg width="70" height="50" viewBox="0 0 70 50"><rect width="70" height="50" rx="10" fill="#222" opacity=".8"/><path d="M28 15 L48 25 L28 35Z" fill="#fff"/></svg>
    </div>
  </div>
</section>
<section class="request">
  <h2 class="sec-title">Request more <b>information</b></h2>
  <div class="form">
    <div class="field">Enter Full Name</div><div class="field">Enter Phone No</div><div class="field">Enter your Email</div>
    <div class="field msg">Message</div><div class="submit">SUBMIT</div>
  </div>
</section>
<section class="team">
  <h2 class="sec-title">Our healthcare <b>team</b></h2>
  <div class="team-grid">
    <div class="card"><div class="photo ph" role="img" aria-label="Portrait of doctor"></div><h3>DR. ARVEN MEHTA</h3><div class="role">Cardiology</div><p>Neque porro quisquam est qui dolorem ipsum quia dolor sit amet, consectetur.</p></div>
    <div class="card"><div class="photo ph" role="img" aria-label="Portrait of doctor"></div><h3>DR. ARVEN MEHTA</h3><div class="role">Cardiology</div><p>Neque porro quisquam est qui dolorem ipsum quia dolor sit amet, consectetur.</p></div>
    <div class="card"><div class="photo ph" role="img" aria-label="Portrait of doctor"></div><h3>DR. ARVEN MEHTA</h3><div class="role">Cardiology</div><p>Neque porro quisquam est qui dolorem ipsum quia dolor sit amet, consectetur.</p></div>
    <div class="card"><div class="photo ph" role="img" aria-label="Portrait of doctor"></div><h3>DR. ARVEN MEHTA</h3><div class="role">Cardiology</div><p>Neque porro quisquam est qui dolorem ipsum quia dolor sit amet, consectetur.</p></div>
  </div>
  <div class="pager"><span></span><span></span></div>
</section>
<section class="partners">
  <h2 class="sec-title">Our <b>partner</b> hospitals</h2>
  <div class="logos"><span></span><span></span><span></span><span></span><span></span><span></span></div>
</section>
<section class="quote">
  <div class="mark">&ldquo;&rdquo;</div>
  <p>I am very much impressed by the arrangements made by Kestrow Care. We were treated with respect and got the support from the staff all the time. I am thankful to the entire team for good work.</p>
  <div class="who"><span class="avatar ph" role="img" aria-label="Customer portrait"></span>Riya Solan</div>
</section>
<footer class="footer">
  <h4>GET IN TOUCH !</h4>
  <div class="contact"><div class="name">Kestrow Care</div><div>Telephone : +91 80 4100 2200</div><div>Email : info@kestrowcare.com</div></div>
  <div><div class="social"><span></span><span></span><span></span><span></span><span></span></div><div class="copy">@copyright 2015 kestrowcare.com</div></div>
</footer>
</body>
</html>
```